Business Card Design needed for start up company Pramora

In need of a new business card designed for a start up company based in Sydney, Pramora is a new start up innovative Company, our mission it to make property accessible for everyday Australian and to become the leading Real Estate platform in Australia. We want it to be fresh and clean.

Industry/Entity Type

Financial

Contact Information for Business Card

Section for Name
Section for Title

PRAMORA - Where Doors Open Wide
Mobile:
Direct:

Font styles to use
Sans Serif

Colors
33a6d7
0692cd
0255a3
ffffff

Requirements
Must have
• Logo, all business card details

```html
<!DOCTYPE html>
<html lang="en">
<head>
<meta charset="utf-8">
<title>Pramora Business Card</title>
<link rel="stylesheet" href="https://fonts.googleapis.com/css2?family=Open+Sans:wght@400;600;700;800&display=swap">
<style>
  :root {
    --navy: #1a4b86;
    --sky: #2a9ad6;
    --white: #ffffff;
    --grey-text: #6b6b6b;
    --backdrop: #2f2f31;
  }
  * { margin: 0; padding: 0; box-sizing: border-box; }
  html, body {
    width: 1200px; height: 864px; overflow: hidden;
    background: var(--backdrop);
    font-family: "Open Sans", sans-serif;
  }
  .stage {
    width: 1200px; height: 864px;
    display: flex; flex-direction: column; align-items: center; justify-content: center;
    gap: 56px;
  }
  .card {
    position: relative;
    width: 540px; height: 309px;
    overflow: hidden;
    box-shadow: 0 10px 24px rgba(0,0,0,0.45);
  }
  /* Front */
  .card-front { background: var(--navy); }
  .brand {
    display: flex; align-items: center; gap: 12px;
    font-weight: 800; letter-spacing: 1px;
  }
  .brand-dot { border-radius: 50%; background: var(--sky); flex: none; }
  .card-front .brand {
    position: absolute; left: 50%; top: 112px; transform: translateX(-50%);
    color: var(--white); font-size: 52px; line-height: 1;
  }
  .card-front .brand-dot { width: 60px; height: 60px; }
  .tagline {
    position: absolute; left: 0; right: 0; bottom: 38px;
    text-align: center; color: var(--white); font-size: 14px; letter-spacing: 0.5px;
  }
  /* Back */
  .card-back { background: var(--white); }
  .card-back .panel { position: absolute; inset: 0; }
  .card-back .brand {
    position: absolute; left: 26px; top: 38px;
    color: var(--navy); font-size: 36px; line-height: 1;
  }
  .card-back .brand-dot { width: 44px; height: 44px; }
  .person { position: absolute; left: 44px; top: 142px; }
  .person-name { color: var(--navy); font-size: 20px; font-weight: 700; line-height: 1.1; }
  .person-title { color: var(--grey-text); font-size: 13px; }
  .contact-list {
    position: absolute; left: 44px; top: 202px;
    list-style: none; color: var(--grey-text); font-size: 13px; line-height: 21px;
  }
  .contact-list li { display: flex; align-items: center; gap: 9px; }
  .contact-list svg { width: 13px; height: 13px; flex: none; }
  .address {
    position: absolute; left: 400px; bottom: 28px;
    color: var(--white); font-size: 11.5px; line-height: 16px;
  }
</style>
</head>
<body>
<main class="stage">
  <section class="card card-front" aria-label="Card front">
    <div class="brand"><span class="brand-dot"></span><span class="brand-name">PRAMORA</span></div>
    <p class="tagline">Where Doors Open Wide</p>
  </section>

  <section class="card card-back" aria-label="Card back">
    <svg class="panel" viewBox="0 0 540 309" preserveAspectRatio="none">
      <polygon points="372,0 382,0 392,309 384,309" fill="var(--sky)"/>
      <polygon points="388,0 540,0 540,309 400,309" fill="var(--navy)"/>
    </svg>
    <div class="brand"><span class="brand-dot"></span><span class="brand-name">PRAMORA</span></div>
    <div class="person">
      <p class="person-name">Daniel Hart</p>
      <p class="person-title">President</p>
    </div>
    <ul class="contact-list">
      <li><svg viewBox="0 0 16 16"><path d="M3 1l3 3-2 2c1 2 3 4 5 5l2-2 3 3-2 3C6 15 1 10 0 4z" fill="var(--sky)"/></svg>01 012-345-6789</li>
      <li><svg viewBox="0 0 16 16"><rect x="4" y="1" width="8" height="14" rx="1.5" fill="none" stroke="var(--sky)" stroke-width="1.6"/></svg>01 012-345-6780</li>
      <li><svg viewBox="0 0 16 16"><rect x="1" y="3" width="14" height="10" fill="none" stroke="var(--sky)" stroke-width="1.4"/><path d="M1 3l7 6 7-6" fill="none" stroke="var(--sky)" stroke-width="1.4"/></svg>info@yourwebsite.com</li>
      <li><svg viewBox="0 0 16 16"><circle cx="8" cy="8" r="6.5" fill="none" stroke="var(--sky)" stroke-width="1.4"/><ellipse cx="8" cy="8" rx="3" ry="6.5" fill="none" stroke="var(--sky)" stroke-width="1.2"/><path d="M1.5 8h13" stroke="var(--sky)" stroke-width="1.2"/></svg>yourwebsite.com</li>
    </ul>
    <p class="address">Street Name, Suite 000<br>State, Zip Code, Country</p>
  </section>
</main>
</body>
</html>
```